Brovalin ERP Campaign Newsletter

Purpose of Document: Professional consulting firm looking to provide prospects with information about our ERP offerings and how we can support them with their ERP implementations. Often we have prospects that are in the middle of implementation and decide they need support.
What are we looking for: Professional look. Please use the attached ERP V5 document brochure content. We are looking for new graphics and layout that makes the content pop. Below is our website and attached company color skus. We want to keep our theme/colors consistent with the website.
Website: https://brovalinconsulting.example/

Target Market(s)

Target prospects in industries including manufacturing and distribution, supply chain and logistics, and professional services.

Industry/Entity Type

Consulting

Requirements
Must have
• Visual graphics

```html
<!DOCTYPE html>
<html lang="en">
<head>
<meta charset="utf-8">
<title>Brovalin ERP Newsletter</title>
<link href="https://fonts.googleapis.com/css2?family=Inter:wght@400;500;600;700;800&display=swap" rel="stylesheet">
<style>
:root{
  --navy-dark:#0f2035;
  --navy:#0f2a4a;
  --blue-hero:#1a4c84;
  --blue-1:#22609e;
  --blue-2:#143d6c;
  --blue-3:#0e2a4d;
  --yellow:#f2c318;
  --grey-text:#666c73;
  --band:#eef3fa;
  --white:#ffffff;
}
*{box-sizing:border-box;margin:0;padding:0}
html,body{width:1200px;height:2754px;overflow:hidden;background:var(--white);font-family:'Inter',sans-serif}
.page{position:relative;width:1200px;height:2754px}
.masthead{position:absolute;left:0;top:0;width:1200px;height:144px;background:var(--navy-dark);display:flex;align-items:center;justify-content:center}
.brand{color:#d8dde3;font-size:84px;font-weight:500;letter-spacing:1px;display:flex;align-items:center;gap:18px}
.brand-mark{width:22px;height:22px;background:var(--yellow)}
.hero{position:absolute;left:0;top:144px;width:1200px;height:574px;background:radial-gradient(ellipse at 70% 90%,#2f6fae 0%,var(--blue-hero) 45%,#113a68 100%)}
.section-title{position:absolute;left:0;width:100%;text-align:center;font-weight:800;font-size:43px;letter-spacing:.3px}
.underline{position:absolute;left:560px;width:80px;height:4px;background:var(--yellow)}
.hero .section-title{top:48px;color:var(--white)}
.hero .underline{top:104px}
.hero-art{position:absolute;left:42px;top:130px;width:410px;height:356px;border-radius:8px;background:linear-gradient(135deg,rgba(180,195,215,.35),rgba(30,80,140,.2))}
.hero-copy{position:absolute;left:486px;top:142px;width:646px;color:var(--white);font-size:22.5px;line-height:35px}
.hero-copy p+p{margin-top:20px}
.services-title{top:758px;color:var(--navy)}
.services-line{top:814px}
.service{position:absolute;top:883px;height:453px;color:var(--white);padding:100px 34px 0 38px}
.service.s1{left:0;width:394px;background:var(--blue-1)}
.service.s2{left:403px;width:394px;background:var(--blue-2);padding-left:42px}
.service.s3{left:806px;width:394px;background:var(--blue-3);padding-left:36px}
.service-icon{position:absolute;top:-36px;width:100px;height:100px;border-radius:50%;background:var(--yellow);display:flex;align-items:center;justify-content:center}
.service h3{font-size:30px;font-weight:700;line-height:40px}
.service .desc{margin-top:12px;font-size:17.5px;line-height:24px}
.service ul{list-style:none;margin-top:22px;font-size:15.5px;line-height:21.5px}
.service li{padding-left:16px;position:relative}
.service li::before{content:"›";position:absolute;left:0;top:-2px;color:var(--yellow);font-weight:700;font-size:19px}
.value-title{position:absolute;left:0;top:1388px;width:100%;text-align:center;font-size:43px;font-weight:700;line-height:54px;color:var(--navy)}
.timeline{position:absolute;left:117px;top:1690px;width:3px;height:540px;background:var(--blue-2)}
.value-icon{position:absolute;left:56px;width:126px;height:126px;border-radius:50%;border:3px solid var(--blue-2);background:var(--white);display:flex;align-items:center;justify-content:center}
.value-icon::after{content:"";position:absolute;inset:8px;border-radius:50%;border:2px solid var(--blue-2)}
.value-text{position:absolute;left:216px;width:920px}
.value-text h4{font-size:28px;font-weight:700;color:var(--blue-2)}
.value-text p{margin-top:12px;font-size:21px;line-height:27px;color:var(--grey-text)}
.platforms{position:absolute;left:0;top:2434px;width:1200px;height:194px;background:var(--band)}
.platforms h5{position:absolute;left:88px;top:72px;font-size:43px;font-weight:700;color:var(--navy-dark)}
.partner{position:absolute;top:56px;display:flex;align-items:center;gap:16px;font-size:30px;font-weight:500;line-height:38px;color:#2c3c55;white-space:nowrap}
.partner .dot{flex:none;width:30px;height:30px;background:var(--blue-2)}
.partner.p1{left:376px}
.partner.p2{left:700px}
.partner.p2 .dot{background:#c5312a;border-radius:50%}
.footer{position:absolute;left:0;top:2664px;width:100%;text-align:center;font-size:24px;color:var(--grey-text)}
</style>
</head>
<body>
<div class="page">
  <header class="masthead"><div class="brand"><span class="brand-mark"></span>Brovalin</div></header>

  <section class="hero">
    <h2 class="section-title">OUR APPROACH</h2>
    <div class="underline"></div>
    <div class="hero-art" role="img" aria-label="Large decorative brand letter with scattered blue and yellow pixel squares"></div>
    <div class="hero-copy">
      <p>Our approach is to give you what you need to get the most from your ERP implementation. If you know what that is, we can leverage a resource base of over 200 ERP consultants, both onshore and off, to provide the expertise that will fit seamlessly into your team.</p>
      <p>If you don’t know what you need, we have a process to help you figure that out. Our eight-point assessment starts with strategy and covers the other seven essential elements that ensure implementation success.</p>
    </div>
  </section>

  <h2 class="section-title services-title">OUR SERVICES</h2>
  <div class="underline services-line"></div>

  <div class="service s1">
    <div class="service-icon" style="left:40px">
      <svg width="58" height="58" viewBox="0 0 58 58" fill="none" stroke="#fff" stroke-width="2.5"><path d="M20 52v-10c-6-4-9-10-9-17a18 18 0 0 1 36 0l5 9h-5v8a4 4 0 0 1-4 4h-5v6"/><circle cx="29" cy="24" r="6"/><circle cx="29" cy="24" r="10" stroke-dasharray="4 3"/></svg>
    </div>
    <h3>ERP<br>Implementations</h3>
    <p class="desc">Select and implement the right ERP platform for your needs and objectives</p>
    <ul><li>Start to Finish Implementations</li><li>Project Turnarounds</li><li>Hard to Find Resources</li><li>Value Add Solutions</li></ul>
  </div>

  <div class="service s2">
    <div class="service-icon" style="left:46px">
      <svg width="60" height="60" viewBox="0 0 60 60" fill="none" stroke="#fff" stroke-width="2.5"><circle cx="20" cy="20" r="8"/><circle cx="40" cy="20" r="8"/><circle cx="30" cy="28" r="8"/><path d="M8 52v-8a10 10 0 0 1 10-10M52 52v-8a10 10 0 0 0-10-10M16 54v-8a10 10 0 0 1 10-10h8a10 10 0 0 1 10 10v8"/></svg>
    </div>
    <h3>ERP Leadership<br>&amp; Staffing</h3>
    <p class="desc">Secure top match talent from interim CIOs to software engineers and project managers</p>
    <ul><li>Strategy Focused Leadership<br>and Expertise</li><li>Right-sized for Your Business</li><li>Maximize ROI</li><li>Lead from Experience</li></ul>
  </div>

  <div class="service s3">
    <div class="service-icon" style="left:40px">
      <svg width="60" height="60" viewBox="0 0 60 60" fill="none" stroke="#fff" stroke-width="2.5"><path d="M22 44c0-6-8-9-8-19a16 16 0 0 1 32 0c0 10-8 13-8 19z"/><path d="M23 49h14M25 54h10"/><circle cx="30" cy="25" r="6"/><path d="M30 4v4M8 25h4M48 25h4M14 10l3 3M46 10l-3 3"/></svg>
    </div>
    <h3>ERP Transformation<br>&amp; &nbsp;Strategy</h3>
    <p class="desc">Define and execute your transformation strategy and clarify technologies to make it real.</p>
    <ul><li>Strategy and Innovation</li><li>Digital and Technology<br>Prioritization &amp; Roadmap</li><li>Executive Coaching</li><li>Process Adoption &amp; Optimization</li></ul>
  </div>

  <h2 class="value-title">Bringing the Most Value to<br>Your ERP Implementation</h2>
  <div class="timeline"></div>

  <div class="value-icon" style="top:1564px">
    <svg width="60" height="60" viewBox="0 0 60 60" fill="none" stroke="#143d6c" stroke-width="2.5"><circle cx="22" cy="22" r="10" stroke-dasharray="5 3"/><circle cx="22" cy="22" r="4"/><circle cx="40" cy="40" r="9" stroke-dasharray="5 3"/><circle cx="40" cy="40" r="3.5"/></svg>
  </div>
  <div class="value-text" style="top:1568px">
    <h4>Emphasis on Process Improvement and Adoption</h4>
    <p>You want to improve processes and ensure adoption. &nbsp;We can help you do both. Brovalin evaluates current processes, identifying process streamlining opportunities along with providing process insight to the ERP implementations. This enables an ERP implementation tailored to your business resulting in increased adoption</p>
  </div>

  <div class="value-icon" style="top:1785px">
    <svg width="62" height="62" viewBox="0 0 62 62" fill="none" stroke="#143d6c" stroke-width="2.5"><circle cx="44" cy="14" r="8"/><path d="M44 10v8"/><rect x="16" y="20" width="16" height="5"/><rect x="16" y="26" width="16" height="5"/><rect x="16" y="32" width="16" height="5"/><path d="M6 40h10l10 4h10a3 3 0 0 1 0 6H24M36 48l14-8a3 3 0 0 1 4 4l-16 12H6"/></svg>
  </div>
  <div class="value-text" style="top:1812px">
    <h4>Bringing Down Costs with the Right Resources</h4>
    <p>If you’re looking for one resource or twenty, working on-site or remote, onshore or off, we can provide them</p>
  </div>

  <div class="value-icon" style="top:2007px">
    <svg width="62" height="62" viewBox="0 0 62 62" fill="none" stroke="#143d6c" stroke-width="2.5"><rect x="12" y="14" width="38" height="28" rx="2"/><path d="M6 46h50l-3 4H9z"/><path d="M22 20h18v10H30l-5 4v-4h-3z"/><path d="M27 25l3 3 5-5"/></svg>
  </div>
  <div class="value-text" style="top:2014px">
    <h4>Need to Add Value to Your Current Installation?</h4>
    <p>If you need help to drive the most value from a system already in production, whether it is business intelligence, Flowline Platform applications, integrations, or new features, we can help.</p>
  </div>

  <div class="value-icon" style="top:2229px">
    <svg width="62" height="62" viewBox="0 0 62 62" fill="none" stroke="#143d6c" stroke-width="2.5"><rect x="12" y="10" width="38" height="34" rx="2"/><path d="M12 18h38M26 44l-3 8M36 44l3 8M20 52h22"/><circle cx="31" cy="31" r="6" stroke-dasharray="4 2.5"/><circle cx="31" cy="31" r="2"/></svg>
  </div>
  <div class="value-text" style="top:2240px">
    <h4>Not Sure What You Need?</h4>
    <p>If you sense something is wrong with your implementation but don’t know what it is, we can help. &nbsp;Our eight-point assessment starts with strategy and continues with the seven things that ensure success.</p>
  </div>

  <section class="platforms">
    <h5>Platforms</h5>
    <div class="partner p1"><span class="dot"></span><span>Corvane<br>Ledger 365</span></div>
    <div class="partner p2"><span class="dot"></span><span>Tallis<br>CloudSuite</span></div>
  </section>

  <footer class="footer">© 2022 Company Name | All Rights Reserved</footer>
</div>
</body>
</html>
```